Creative - Appealing - Business Card Design Project

Looking for a Business card design (vector artwork) for an existing company called 'Fernway Sound'. We operate in the entertainment industry specializing in audio system design and rental, however; we also deal with other sectors of the entertainment industry including lighting, video, staging and power system design and rental. We would like to see designs that don't focus too much on audio but include elements encompassing everything else.

Double sided business card, following our new colour scheme and logo, which is attached. The card would ideally be creative and eye catching to draw in new customers in the elegant event production market, such as weddings & corporate affairs.

Target Market(s)

High end corporate clients, wedding clients

Industry/Entity Type

Entertainment

Requirements
Must have
• Our contact details, these can be worded & listed however you think appropriate as part as the design

Business Name - Fernway Sound
My Name - Dominic Harwell
Web Address - www.fernwaysound-example.com
Mobile Number - 07914 362 517
Office Number - 0330 481 7265
Email - dom@fernwaysound-example.com

The name, email and mobile number would need to be able to be changed to my business partners also.

The font used on our logo is Sansation
Nice to have
• On one side maybe a word cloud involving the services in which we can provide; Lighting, Sound, Event Production, Staging, LED Uplighting, Projection Mapping, Wedding Hire

On the other side, all the important credentials of contact.
Should not have
• The design should not use any old style fonts (i.e Times New Roman, Gothic etc) or on the other side of the scale, any 'jokey' fonts (i.e. Comic Sans).

The font to be used is Sansation

```html
<!DOCTYPE html>
<html lang="en">
<head>
<meta charset="utf-8">
<title>Fernway Sound – Business Card</title>
<link href="https://fonts.googleapis.com/css2?family=Sansation:wght@400;700&display=swap" rel="stylesheet">
<style>
  :root {
    --stage: #e9e6e3;
    --card: #ffffff;
    --purple: #4b3489;
    --purple-deep: #342563;
    --purple-soft: #8f84c2;
    --grey: #8a8a8a;
    --grey-dark: #5e5e5e;
    --ink: #222222;
    --label: #2b2b2b;
  }
  * { box-sizing: border-box; margin: 0; padding: 0; }
  html, body { width: 1200px; height: 800px; overflow: hidden; }
  body {
    position: relative;
    background: var(--stage);
    font-family: "Sansation", sans-serif;
    color: var(--ink);
  }
  .side-label {
    position: absolute;
    width: 510px;
    text-align: center;
    font-size: 21px;
    color: var(--label);
  }
  .card {
    position: absolute;
    width: 510px;
    height: 290px;
    border-radius: 22px;
    background: var(--card);
    overflow: hidden;
    box-shadow: 0 4px 12px rgba(0,0,0,.18);
  }
  .card--front  { left: 70px;  top: 90px; }
  .card--back-1 { left: 621px; top: 90px; }
  .card--back-2 { left: 70px;  top: 450px; }
  .card--back-3 {
    left: 621px; top: 450px;
    background: linear-gradient(90deg, var(--purple-deep) 0%, var(--purple) 55%, var(--purple-soft) 100%);
  }

  /* Front */
  .front-band {
    position: absolute; left: 0; top: 138px; width: 100%; height: 52px;
    background: var(--purple);
  }
  .front-wordmark {
    position: absolute; left: 57px; top: 128px; width: 195px; height: 72px;
    background: var(--card);
    display: flex; align-items: center; justify-content: center;
    font-size: 26px; font-weight: 700; color: var(--grey);
    text-align: center; line-height: 1;
  }
  .front-name {
    position: absolute; left: 253px; top: 138px; width: 257px; height: 52px;
    background: linear-gradient(90deg, var(--purple) 0%, var(--purple) 55%, var(--purple-soft) 100%);
    display: flex; align-items: center; padding-left: 36px;
    color: #fff; font-size: 17px; font-weight: 700;
  }
  .contact-list {
    position: absolute; top: 230px; list-style: none;
    font-size: 13.5px; color: var(--ink); line-height: 21px;
  }
  .contact-list--phones { left: 64px; }
  .contact-list--web { left: 212px; }
  .contact-list li { display: flex; align-items: center; gap: 5px; }
  .contact-list svg { width: 11px; height: 11px; fill: var(--purple); flex: none; }

  /* Service lists */
  .provide-title { font-weight: 700; color: var(--purple); font-size: 15px; }
  .service {
    display: inline-flex; align-items: center; gap: 2px;
    color: var(--grey); font-size: 15px;
  }
  .service::before {
    content: ""; width: 9px; height: 9px; background: currentColor;
    clip-path: polygon(50% 0, 62% 55%, 100% 100%, 50% 75%, 0 100%, 38% 55%);
  }
  .web-address {
    position: absolute; left: 0; width: 100%; text-align: center;
    font-size: 13px; letter-spacing: 2.2px; color: var(--ink);
  }

  /* Back 1 */
  .back1-wordmark {
    position: absolute; left: 0; top: 106px; width: 100%; text-align: center;
    font-size: 26px; font-weight: 700; color: var(--grey);
  }
  .back1-services {
    position: absolute; left: 0; top: 178px; width: 100%; text-align: center;
  }
  .back1-services .provide-title { margin-bottom: 6px; }
  .service-row { display: flex; justify-content: center; gap: 6px; line-height: 23px; }
  .card--back-1 .web-address { top: 258px; }

  /* Back 2 */
  .back2-mark {
    position: absolute; left: 34px; top: 25px; width: 200px; height: 225px;
    display: flex; align-items: center; justify-content: center;
    font-size: 40px; font-weight: 700; color: var(--purple);
    line-height: 1.1; text-align: left;
  }
  .back2-services {
    position: absolute; left: 284px; top: 45px; list-style: none;
  }
  .back2-services .provide-title { margin-bottom: 4px; }
  .back2-services li { line-height: 23.5px; }
  .back2-services .service { gap: 7px; }
  .card--back-2 .web-address { top: 260px; }

  /* Back 3 */
  .back3-services {
    position: absolute; left: 0; top: 56px; width: 100%; text-align: center; color: #fff;
  }
  .back3-services .provide-title { color: #fff; margin-bottom: 12px; }
  .back3-services .service-row { line-height: 33.5px; gap: 8px; }
  .back3-services .service { color: #fff; }
  .card--back-3 .web-address { top: 258px; color: #fff; }
</style>
</head>
<body>
  <div class="side-label" style="left:74px;top:50px;">Front</div>
  <div class="side-label" style="left:632px;top:50px;">Back - 1</div>
  <div class="side-label" style="left:74px;top:410px;">Back - 2</div>
  <div class="side-label" style="left:632px;top:410px;">Back - 3</div>

  <section class="card card--front">
    <div class="front-band"></div>
    <div class="front-wordmark">FERNWAY<br>SOUND</div>
    <div class="front-name">Dominic Harwell</div>
    <ul class="contact-list contact-list--phones">
      <li><svg viewBox="0 0 12 12"><rect x="3" y="0" width="6" height="12" rx="1.2"/></svg>07914 362 517</li>
      <li><svg viewBox="0 0 12 12"><path d="M1 4c0-2 3-3 5-3s5 1 5 3l-2 1-1-1H4L3 5zM2 6h8l1 5H1z"/></svg>0330 481 7265</li>
    </ul>
    <ul class="contact-list contact-list--web">
      <li><svg viewBox="0 0 12 12"><path d="M1 3h10v7H1zM1 3l5 4 5-4"/></svg>dom@fernwaysound-example.com</li>
      <li><svg viewBox="0 0 12 12"><circle cx="6" cy="6" r="5.5" fill="none" stroke="#4b3489" stroke-width="1.2"/><path d="M0.5 6h11M6 .5v11" stroke="#4b3489" stroke-width="1"/></svg>www.fernwaysound-example.com</li>
    </ul>
  </section>

  <section class="card card--back-1">
    <div class="back1-wordmark">FERNWAY SOUND</div>
    <div class="back1-services">
      <div class="provide-title">WE CAN PROVIDE</div>
      <div class="service-row"><span class="service">Lighting</span><span class="service">Sound</span><span class="service">Event Production</span><span class="service">Staging</span></div>
      <div class="service-row"><span class="service">LED Uplighting</span><span class="service">Projection Mapping</span><span class="service">Wedding Hire</span></div>
    </div>
    <div class="web-address">www.fernwaysound-example.com</div>
  </section>

  <section class="card card--back-2">
    <div class="back2-mark">FERNWAY<br>SOUND</div>
    <ul class="back2-services">
      <li class="provide-title">WE CAN PROVIDE</li>
      <li class="service">Lighting</li><br>
      <li class="service">Sound</li><br>
      <li class="service">Event Production</li><br>
      <li class="service">Staging</li><br>
      <li class="service">LED Uplighting</li><br>
      <li class="service">Projection Mapping</li><br>
      <li class="service">Wedding Hire</li>
    </ul>
    <div class="web-address">www.fernwaysound-example.com</div>
  </section>

  <section class="card card--back-3">
    <div class="back3-services">
      <div class="provide-title">WE CAN PROVIDE</div>
      <div class="service-row"><span class="service">Lighting</span><span class="service">Sound</span></div>
      <div class="service-row"><span class="service">Event Production</span><span class="service">Staging</span></div>
      <div class="service-row"><span class="service">LED Uplighting</span><span class="service">Projection Mapping</span></div>
      <div class="service-row"><span class="service">Wedding Hire</span></div>
    </div>
    <div class="web-address">www.fernwaysound-example.com</div>
  </section>
</body>
</html>
```